VENTURE CAPITAL GROUP BUSINESS CARD DESIGN

Venture Capital Group based in SF looking for a bold business card design. No trendy colour explosion, 3D effects etc. Just "simple" optical effects. Works on your brain, keeps your eye focused and sticks to your mind.
Target Market(s)
Technology startups
Industry/Entity Type
Venture Capital
Contact Information for Business Card
BARTHOLOMEW ELLING
MANAGING PARTNER
817 FERN ST SAN FRANCISCO, CA 94111
415.555.0142 O
415.555.0187 F
415.555.0236 C
bart@quillbrookfunds.example

```html
<!DOCTYPE html>
<html lang="en">
<head>
<meta charset="utf-8">
<title>Quillbrook Capital Group – Business Card</title>
<link rel="stylesheet" href="https://fonts.googleapis.com/css2?family=Open+Sans:ital,wght@0,400;0,600;0,700;1,400&display=swap">
<style>
  :root {
    --stage: #e9e7e2;
    --card-white: #ffffff;
    --green: #2f8f3a;
    --green-dark: #1f6e2a;
    --grey-text: #8a8a8a;
    --ink: #3c3c3c;
    --rule: #c9c9c9;
    --back-top: #9a9a9a;
    --back-bottom: #5e5e5e;
    --white: #ffffff;
  }
  * { box-sizing: border-box; margin: 0; padding: 0; }
  html, body { width: 1200px; height: 950px; overflow: hidden; }
  body {
    background: var(--stage);
    font-family: "Open Sans", Arial, sans-serif;
    position: relative;
  }
  .card {
    position: absolute;
    top: 327px;
    width: 520px;
    height: 296px;
    border-radius: 16px;
    box-shadow: 0 10px 26px rgba(0,0,0,.18);
    overflow: hidden;
  }
  /* ---------- front ---------- */
  .card-front { left: 60px; background: var(--card-white); border-bottom: 5px solid var(--green); }
  .brand {
    position: absolute; top: 44px; left: 166px;
    display: flex; align-items: center; gap: 12px;
  }
  .brand-dot { width: 40px; height: 40px; border-radius: 50%; background: var(--green); flex: none; }
  .brand-name {
    color: var(--green);
    font-weight: 600;
    letter-spacing: .08em;
    line-height: 1.1;
    white-space: nowrap;
  }
  .brand-name .word { display: block; font-size: 22px; }
  .brand-name .sub { display: block; font-size: 9px; letter-spacing: .32em; }
  .brand-divider {
    position: absolute; top: 34px; left: 400px;
    width: 1px; height: 72px; background: var(--rule);
  }
  .address {
    position: absolute; top: 42px; right: 28px;
    text-align: right; color: var(--ink);
    font-size: 11.5px; line-height: 1.55; font-style: normal;
  }
  .person { position: absolute; left: 34px; top: 148px; }
  .person-name { color: var(--green); font-size: 20px; font-weight: 700; letter-spacing: .01em; line-height: 1.35; }
  .person-title {
    color: var(--grey-text); font-size: 12px; margin-top: 2px;
    display: flex; align-items: center; gap: 8px;
  }
  .person-title::after { content: ""; width: 140px; height: 1px; background: var(--rule); }
  .contacts { list-style: none; margin-top: 10px; }
  .contacts li {
    display: flex; align-items: center; gap: 8px;
    font-size: 11.5px; color: var(--ink); line-height: 17px;
  }
  .contacts svg { width: 11px; height: 11px; fill: var(--green-dark); flex: none; }
  /* ---------- back ---------- */
  .card-back {
    left: 620px;
    background: linear-gradient(160deg, var(--back-top), var(--back-bottom));
  }
  .back-brand {
    position: absolute; left: 40px; bottom: 70px;
    display: flex; align-items: center; gap: 14px;
    color: var(--white); font-weight: 600; letter-spacing: .08em; line-height: 1.1;
  }
  .back-dot { width: 44px; height: 44px; border-radius: 50%; background: var(--white); flex: none; }
  .back-brand .word { display: block; font-size: 30px; }
  .back-brand .sub { display: block; font-size: 11px; letter-spacing: .4em; }
  .web {
    position: absolute; left: 40px; bottom: 38px;
    color: var(--white); font-size: 12px; font-style: italic; letter-spacing: .02em;
  }
</style>
</head>
<body>
  <section class="card card-front" aria-label="Business card front">
    <div class="brand">
      <span class="brand-dot"></span>
      <span class="brand-name"><span class="word">QUILLBROOK</span><span class="sub">CAPITAL GROUP</span></span>
    </div>
    <span class="brand-divider"></span>
    <address class="address">
      817 Fern ST<br>Daly City<br>CA 94014
    </address>

    <div class="person">
      <h1 class="person-name">Bartholomew Elling</h1>
      <p class="person-title">Managing Partner</p>
      <ul class="contacts">
        <li>
          <svg viewBox="0 0 24 24"><path d="M6.6 10.8a15 15 0 0 0 6.6 6.6l2.2-2.2c.3-.3.7-.4 1-.2 1.1.4 2.3.6 3.6.6.6 0 1 .4 1 1V20c0 .6-.4 1-1 1A17 17 0 0 1 3 4c0-.6.4-1 1-1h3.5c.6 0 1 .4 1 1 0 1.3.2 2.5.6 3.6.1.3 0 .7-.2 1z"/></svg>
          415.555.0142
        </li>
        <li>
          <svg viewBox="0 0 24 24"><path d="M7 1h10a2 2 0 0 1 2 2v18a2 2 0 0 1-2 2H7a2 2 0 0 1-2-2V3a2 2 0 0 1 2-2zm0 3v14h10V4z"/></svg>
          415.555.0236
        </li>
        <li>
          <svg viewBox="0 0 24 24"><path d="M6 2h9l3 3v4h1a3 3 0 0 1 3 3v8H2v-8a3 3 0 0 1 3-3h1zm2 2v5h8V6h-2V4zm8 10v2h2v-2z"/></svg>
          415.555.0187
        </li>
        <li>
          <svg viewBox="0 0 24 24"><path d="M2 4h20v16H2zm2 2v.5l8 5 8-5V6zm0 2.8V18h16V8.8l-8 5z"/></svg>
          bart@quillbrookfunds.example
        </li>
      </ul>
    </div>
  </section>

  <section class="card card-back" aria-label="Business card back">
    <div class="back-brand">
      <span class="back-dot"></span>
      <span><span class="word">QUILLBROOK</span><span class="sub">CAPITAL GROUP</span></span>
    </div>
    <p class="web">www.quillbrookfunds.example</p>
  </section>
</body>
</html>
```